Website for IT consulting Company

I need a website upgrade, the existing site content is ok, I would also like to add a testimonial page, the site should be something that is easy for us to update content. You use the content from www.velmarketa.com as an example. I will also post update logo and artwork. I also need a contact form with some type of validation or captcha.

Please omit Address maps

Target Market(s)

small business, service oriented companies. We provide IT Consulting, support and mangement

Industry/Entity Type

Information Technology

Coding

Coded - Design and coding required

Number of Pages Required

1 page

Font styles to use
Serif
Sans Serif

Requirements
Must have
• Contain logo attached, and content from existing web site www.velmarketa.com.
• Also need to update content easily, and be movable to different platforms.
• There is a catch phrase
• "Let us worry about your technology…” “ so you don’t have to!”
• Should be included.
Nice to have
• Testimonial page, Project page where we can post new and past projects and pictures
Should not have
• none

```html
<!DOCTYPE html>
<html lang="en">
<head>
<meta charset="utf-8">
<title>Velmarketa – Our Projects</title>
<link href="https://fonts.googleapis.com/css2?family=Roboto:ital,wght@0,300;0,400;0,500;1,400&display=swap" rel="stylesheet">
<style>
:root{
  --orange:#f7941d;
  --text:#444;
  --muted:#666;
  --footer:#29313c;
  --footer-line:#3c4551;
  --footer-text:#c9ced5;
  --white:#fff;
  --light:#e8e8e8;
}
*{margin:0;padding:0;box-sizing:border-box}
html,body{width:1200px;height:1168px;overflow:hidden}
body{font-family:'Roboto',sans-serif;color:var(--text);background:var(--white);position:relative}
.site-header{position:absolute;left:0;top:0;width:1200px;height:71px;border-bottom:1px solid #e4e4e4}
.brand{position:absolute;left:89px;top:22px;font-size:24px;font-weight:500;color:#555;line-height:26px}
.main-nav{position:absolute;right:89px;top:0;height:71px;display:flex;align-items:center;gap:32px;font-size:13.5px;color:#333}
.main-nav .active{color:var(--orange);position:relative}
.main-nav .active::before{content:"";position:absolute;left:0;right:0;top:-30px;height:2px;background:var(--orange)}
.page-banner{position:absolute;left:0;top:71px;width:1200px;height:94px;background:linear-gradient(90deg,#5d6a70 0%,#8a97a0 35%,#b7c1c9 60%,#c9d0d6 100%)}
.page-banner h1{position:absolute;left:88px;top:34px;font-size:27px;font-weight:400;color:var(--white)}
.breadcrumb{position:absolute;right:89px;top:43px;font-size:14px;color:var(--white)}
.breadcrumb span{margin:0 12px;font-size:11px}
.categories{position:absolute;left:88px;top:214px;width:236px}
.categories h2{font-size:20px;font-weight:400;color:#333;padding-bottom:10px;border-bottom:1px solid #ddd}
.categories ul{list-style:none;margin-top:18px}
.categories li{font-size:14px;color:var(--muted);height:31px;display:flex;align-items:center;gap:10px}
.box{width:9px;height:9px;background:var(--light);display:inline-block;position:relative}
.box.checked{background:var(--orange)}
.box.checked svg{position:absolute;left:1px;top:1px}
.projects{position:absolute;left:415px;top:220px;width:696px;display:grid;grid-template-columns:repeat(3,232px);grid-auto-rows:241px}
.project{position:relative;color:var(--white);text-align:center}
.project h3{position:absolute;left:0;right:0;bottom:41px;font-size:15px;font-weight:500}
.project p{position:absolute;left:0;right:0;bottom:25px;font-size:12px;font-style:italic}
.site-footer{position:absolute;left:0;top:759px;width:1200px;height:409px;background:var(--footer);color:var(--footer-text)}
.site-footer h2{font-size:19px;font-weight:400;color:var(--white)}
.contact-info{position:absolute;left:88px;top:58px;width:320px}
.contact-info ul{list-style:none;margin-top:18px;font-size:13px;line-height:22px}
.contact-info li{display:flex;gap:9px;margin-bottom:13px}
.contact-info svg{flex:none;margin-top:5px}
.divider{position:absolute;left:509px;top:63px;width:1px;height:240px;background:var(--footer-line)}
.contact-form{position:absolute;left:621px;top:58px;width:490px}
.field-label{position:absolute;font-size:15px;color:var(--white)}
.field{position:absolute;font-size:12px;color:var(--footer-text);border-bottom:1px solid var(--footer-line);padding-bottom:10px}
.captcha{position:absolute;left:2px;top:203px;width:181px;height:44px;background:#f9f9f9;border:1px solid #d3d3d3;border-radius:2px;color:#222;font-size:8px}
.captcha .tick{position:absolute;left:8px;top:14px;width:16px;height:16px;border:2px solid #c1c1c1;border-radius:2px;background:#fff}
.captcha .label{position:absolute;left:30px;top:18px}
.captcha .mark{position:absolute;right:14px;top:7px;width:16px;height:16px;border-radius:50%;background:#4a90e2}
.captcha .sub{position:absolute;right:6px;top:27px;font-size:5px;color:#555;text-align:center;line-height:7px}
.submit{position:absolute;right:0;top:203px;width:114px;height:44px;background:var(--orange);color:var(--white);font-size:15px;display:flex;align-items:center;justify-content:center;gap:14px;border-radius:2px}
.copyright{position:absolute;left:88px;top:358px;width:1023px;border-top:1px solid var(--footer-line);text-align:center;padding-top:20px;font-size:13px;color:var(--white)}
</style>
</head>
<body>
<header class="site-header">
  <div class="brand">Velmarketa</div>
  <nav class="main-nav">
    <span>About us</span><span class="active">Projects</span><span>Support</span><span>Clients</span><span>Careers</span><span>Testimonials</span><span>Contact</span>
    <svg width="14" height="14" viewBox="0 0 14 14" fill="none" stroke="#333" stroke-width="1.3"><circle cx="6" cy="6" r="4.8"/><path d="M9.5 9.5L13 13"/></svg>
  </nav>
</header>

<section class="page-banner" role="img" aria-label="Blurred office photo with people at work">
  <h1>Our Projects</h1>
  <div class="breadcrumb">Home<span>&gt;</span>Projects</div>
</section>

<aside class="categories">
  <h2>Sort by categories</h2>
  <ul>
    <li><i class="box"></i>Network Administration</li>
    <li><i class="box"></i>Desktop Support</li>
    <li><i class="box checked"><svg width="7" height="7" viewBox="0 0 7 7" fill="none" stroke="#fff" stroke-width="1.2"><path d="M1 3.5l1.7 1.7L6 1.8"/></svg></i>Network Cabling</li>
    <li><i class="box"></i>Wireless Networks</li>
    <li><i class="box"></i>Antivirus Solutions</li>
    <li><i class="box"></i>Network Security</li>
    <li><i class="box"></i>Telecommunication Solutions</li>
    <li><i class="box"></i>Disaster Recovery</li>
    <li><i class="box"></i>Audo/Video Multimedia</li>
    <li><i class="box"></i>Web Design</li>
  </ul>
</aside>

<main class="projects">
  <article class="project" role="img" aria-label="Laptop on a wooden desk showing a website" style="background:linear-gradient(180deg,#3b3530,#5a5149 50%,#2f2b28)"><h3>Project 1</h3><p>Turkey</p></article>
  <article class="project" role="img" aria-label="Hands typing on a laptop keyboard" style="background:linear-gradient(135deg,#1f4a44,#6d8a84 50%,#cfd3d0)"><h3>Project 2</h3><p>USA</p></article>
  <article class="project" role="img" aria-label="Laptop on a desk in front of a bookshelf" style="background:linear-gradient(180deg,#6b5a45,#a7a7b8 50%,#9a7c5a)"><h3>Project 2</h3><p>Canada</p></article>
  <article class="project" role="img" aria-label="Person holding a black mug while using a laptop" style="background:linear-gradient(135deg,#e4e0d6,#8f9a6d 50%,#3d3c38)"><h3>Project 1</h3><p>UAE</p></article>
  <article class="project" role="img" aria-label="Hands typing on a laptop in soft light" style="background:linear-gradient(135deg,#4f5a54,#8f8f86 50%,#c7c3bb)"><h3>Project 2</h3><p>Newzeland</p></article>
  <article class="project" role="img" aria-label="Laptop and coffee cup on a wooden table" style="background:linear-gradient(180deg,#4e3d30,#7d6858 50%,#5b4535)"><h3>Project 2</h3><p>South Africa</p></article>
</main>

<footer class="site-footer">
  <div class="contact-info">
    <h2>Contact information</h2>
    <ul>
      <li><svg width="10" height="12" viewBox="0 0 10 12"><path d="M5 0a4 4 0 0 0-4 4c0 3 4 8 4 8s4-5 4-8a4 4 0 0 0-4-4z" fill="#f7941d"/><circle cx="5" cy="4" r="1.5" fill="#29313c"/></svg>Address:Some address line goes here. City name, Country name here.</li>
      <li><svg width="10" height="10" viewBox="0 0 10 10"><path d="M2 0l2 2.5-1 1.3a6 6 0 0 0 3.2 3.2l1.3-1L10 8l-1.5 2C4 10 0 6 0 1.5z" fill="#f7941d"/></svg>Phone: 123 456 7890</li>
      <li><svg width="11" height="8" viewBox="0 0 11 8"><rect width="11" height="8" fill="#f7941d"/><path d="M0 0l5.5 4.5L11 0" fill="none" stroke="#29313c"/></svg>Email: info@velmarketa.com</li>
      <li><svg width="11" height="10" viewBox="0 0 11 10"><rect x="2.5" y="0" width="6" height="3" fill="#f7941d"/><rect x="0" y="3.5" width="11" height="4" fill="#f7941d"/><rect x="2.5" y="7" width="6" height="3" fill="#f7941d"/></svg>Fax: 123 546 7890</li>
    </ul>
  </div>
  <div class="divider"></div>
  <form class="contact-form">
    <h2>Contact now</h2>
    <span class="field-label" style="left:0;top:48px">Name:</span>
    <span class="field" style="left:1px;top:79px;width:235px">Enter your name...</span>
    <span class="field-label" style="left:254px;top:48px">Email:</span>
    <span class="field" style="left:255px;top:79px;width:235px">Enter your email...</span>
    <span class="field-label" style="left:0;top:116px">Message:</span>
    <span class="field" style="left:1px;top:146px;width:489px;padding-bottom:30px">Enter your message...</span>
    <div class="captcha"><span class="tick"></span><span class="label">I'm not a robot</span><span class="mark"></span><span class="sub">HumanCheck<br>Privacy - Terms</span></div>
    <div class="submit">Submit <svg width="10" height="8" viewBox="0 0 10 8" fill="none" stroke="#fff" stroke-width="1.1"><path d="M0 4h9M6 1l3 3-3 3"/></svg></div>
  </form>
  <div class="copyright">© 2017, All Rights Reserved.</div>
</footer>
</body>
</html>
```